Letterhead, business cards, envelopes
Thornwell Holdings Property Management
Creative Brief
Professional
Dean Pultorak
Real Estate Asset Manager
27816 Brisbane Ave., Fenwick Ca 90815
dean@thpropertymgmt.example
www.thpropertymgmt.example
designers choice

```html
<!DOCTYPE html>
<html lang="en">
<head>
<meta charset="utf-8">
<title>Thornwell Holdings Property Management — Stationery</title>
<link href="https://fonts.googleapis.com/css2?family=Open+Sans:wght@400;600;700&display=swap" rel="stylesheet">
<style>
:root{
  --bg:#3d322b;
  --paper:#ffffff;
  --green:#1f6a3b;
  --ink:#2b2b2b;
  --grey:#8a8a8a;
  --faint:#f1f1f1;
  --line:#c9c9c9;
}
*{box-sizing:border-box;margin:0;padding:0}
html,body{width:1200px;height:952px;overflow:hidden}
body{background:var(--bg);position:relative;font-family:"Open Sans",Arial,sans-serif;color:var(--ink)}
.sheet,.card,.envelope{position:absolute;background:var(--paper);box-shadow:0 4px 10px rgba(0,0,0,.35);overflow:hidden}

/* name with plain square */
.brand{display:flex;align-items:center;gap:6px}
.brand-square{width:22px;height:22px;background:var(--green);flex:none}
.brand-name{font-family:"Open Sans",Arial,sans-serif;font-weight:700;color:var(--green);font-size:9px;line-height:1.2;text-transform:uppercase;letter-spacing:.2px}

.contact{font-size:6px;line-height:1.5;color:var(--grey)}

/* letter sheets */
.fax{left:65px;top:103px;width:394px;height:511px}
.letterhead{left:475px;top:103px;width:390px;height:511px}
.sheet .brand{position:absolute;left:20px;top:22px}
.sheet .contact{position:absolute;left:215px;top:14px}
.green-tab{position:absolute;right:0;top:36px;width:56px;height:14px;background:var(--green)}
.watermark{position:absolute;left:50%;top:50%;width:200px;height:200px;transform:translate(-50%,-45%);background:var(--faint)}
.fax-title{position:absolute;right:40px;top:112px;font-weight:700;font-size:20px}
.fax-table{position:absolute;left:20px;top:140px;width:350px;border-collapse:collapse;font-size:7px}
.fax-table td{border:1px solid var(--line);height:15px;padding:0 4px;width:25%}
.fax-comments{position:absolute;left:22px;top:215px;font-size:7px}

/* business cards */
.card{width:258px;border-radius:8px}
.card-contact{left:877px;top:108px;height:150px}
.card-brand{left:877px;top:279px;height:149px}
.card-green{left:877px;top:464px;height:155px;background:var(--green)}
.card .brand{position:absolute;left:50%;transform:translateX(-50%);white-space:nowrap}
.card-contact .brand{top:16px}
.card-contact .contact{position:absolute;left:14px;top:74px}
.card-person{position:absolute;right:16px;top:98px;text-align:right}
.card-person .name{font-weight:700;font-size:13px}
.card-person .role{font-size:6px;color:var(--grey)}
.card-brand .brand,.card-green .brand{top:58px}
.card-brand .brand-square,.card-green .brand-square{width:30px;height:30px}
.card-brand .brand-name,.card-green .brand-name{font-size:11px}
.card-green .brand-square{background:#fff}
.card-green .brand-name{color:#fff}

/* envelopes */
.envelope{top:622px;height:198px;width:361px}
.env-back{left:150px}
.env-front{left:529px}
.env-back svg{position:absolute;left:0;top:0}
.env-front .brand{position:absolute;left:14px;top:14px}
.env-front .contact{position:absolute;left:14px;top:46px}
.env-front .faint-square{position:absolute;right:14px;bottom:14px;width:100px;height:100px;background:var(--faint)}

/* standalone name display */
.name-display{position:absolute;left:787px;top:836px;display:flex;align-items:center;gap:12px}
.name-display .brand-square{width:60px;height:60px;background:#fff}
.name-display .brand-name{color:#fff;font-size:17px}
</style>
</head>
<body>

<section class="sheet fax">
  <div class="brand"><div class="brand-square"></div><div class="brand-name">Thornwell Holdings<br>Property Management</div></div>
  <div class="contact">27816 Brisbane Ave.<br>Fenwick Ca 90815<br>T: 714.555.0142<br>F: 714.555.0143<br>dean@thpropertymgmt.example<br>www.thpropertymgmt.example</div>
  <div class="green-tab"></div>
  <div class="watermark" role="img" aria-label="Faint background panel"></div>
  <div class="fax-title">FAX</div>
  <table class="fax-table">
    <tr><td>TO:</td><td></td><td>FROM:</td><td></td></tr>
    <tr><td>FAX:</td><td></td><td>PAGES:</td><td></td></tr>
    <tr><td>PHONE:</td><td></td><td>DATE:</td><td></td></tr>
    <tr><td>RE:</td><td></td><td>CC:</td><td></td></tr>
  </table>
  <div class="fax-comments">COMMENTS:</div>
</section>

<section class="sheet letterhead">
  <div class="brand"><div class="brand-square"></div><div class="brand-name">Thornwell Holdings<br>Property Management</div></div>
  <div class="contact">27816 Brisbane Ave.<br>Fenwick Ca 90815<br>T: 714.555.0142<br>F: 714.555.0143<br>dean@thpropertymgmt.example<br>www.thpropertymgmt.example</div>
  <div class="green-tab"></div>
  <div class="watermark" role="img" aria-label="Faint background panel"></div>
</section>

<section class="card card-contact">
  <div class="brand"><div class="brand-square"></div><div class="brand-name">Thornwell Holdings<br>Property Management</div></div>
  <div class="contact">27816 Brisbane Ave.<br>Fenwick Ca 90815<br>T: 714.555.0142<br>F: 714.555.0143<br>dean@thpropertymgmt.example<br>www.thpropertymgmt.example</div>
  <div class="card-person"><div class="name">Dean Pultorak</div><div class="role">Real Estate Asset Manager</div></div>
</section>

<section class="card card-brand">
  <div class="brand"><div class="brand-square"></div><div class="brand-name">Thornwell Holdings<br>Property Management</div></div>
</section>

<section class="card card-green">
  <div class="brand"><div class="brand-square"></div><div class="brand-name">Thornwell Holdings<br>Property Management</div></div>
</section>

<section class="envelope env-back">
  <svg width="361" height="198" viewBox="0 0 361 198">
    <polygon points="0,0 361,0 181,105" fill="#1f6a3b"/>
    <polyline points="0,198 181,95 361,198" fill="none" stroke="#e2e2e2" stroke-width="1"/>
  </svg>
</section>

<section class="envelope env-front">
  <div class="brand"><div class="brand-square"></div><div class="brand-name">Thornwell Holdings<br>Property Management</div></div>
  <div class="contact">27816 Brisbane Ave.<br>Fenwick Ca 90815</div>
  <div class="faint-square"></div>
</section>

<section class="name-display">
  <div class="brand-square"></div>
  <div class="brand-name">Thornwell Holdings<br>Property Management</div>
</section>

</body>
</html>
```